Design a box that holds medical gloves for paramedics!

We need a design for a box of gloves (nitrile gloves). We are designing this for a specific customer whose name is Brenvo (their logo is attached as image000.1png). We have also attached the current design for the box which we want to change to be specific for Brenvo. Everywhere you see a turtle, replace it with the Brenvo logo. There should be no turtles on the box. The people who use these gloves are paramedics who work in an ambulance. The box should look TOUGH, American, and instill confidence and safety. An American flag alone or one incorporating the eagle from the company logo covering the top of the box (perhaps in the background on the top) would be a nice touch. Do not change anything on the bottom of the box, which is the side with the size chart on it. You can change background color but all the info on the bottom of the box needs to stay there. What you send back should be the box with all sides designed. We need to start showing our customer options right away for this box so please don't hesitate to start. We look forward to working with you.
Updates

The Client has changed his mind regarding the use of an American Flag. This product will be sold world wide, so NO FLAGS AT ALL. We still want the box to look TOUGH. We would like the top of the box to have the Brenvo Logo very LARGE. We would like the Falcon from the logo to be incorporated somehow into the background of the box. So the whole Falcon or wings of the Brenvo faded in background might be nice. The color scheme should still be black, red and white. The design should be bold and tough looking. This initial box will be used for black gloves but in the future the box may have blue gloves so we need some part/aspect of the box to be able to change color to blue or white if we change the color of gloves in the box in the future to have blue or white gloves. Please leave bottom of the box as is shown in original photo uploaded. Thanks and sorry for the change this late in the process.

Target Market(s)

The buyer of this product is a Paramedic who works on an ambulance. Medical market. EMS market.

Industry/Entity Type

Medical

Font styles to use
Sans Serif

Colors
ec1f27
ffffff
1b1b1b

Requirements
Must have
• American Flag
• Patriotic
• Brenvo Logo in several places
• Look tough
• Color scheme should be Black, Red and White.

```html
<!DOCTYPE html>
<html lang="en">
<head>
<meta charset="utf-8">
<title>Brenvo Nitrile Gloves Box</title>
<link href="https://fonts.googleapis.com/css2?family=Open+Sans:wght@400;600;700;800&display=swap" rel="stylesheet">
<style>
  :root {
    --backdrop: #e0e1cb;
    --box-black: #1b1b1b;
    --box-black-light: #3a3a3a;
    --panel-grey: #a3a3a3;
    --brand-red: #ec1f27;
    --white: #ffffff;
    --ink: #111111;
    --glove-blue: #1c2f9e;
    --feature-text: #222222;
  }
  html, body {
    margin: 0;
    padding: 0;
    width: 1200px;
    height: 904px;
    overflow: hidden;
    background: var(--backdrop);
    font-family: "Open Sans", Arial, sans-serif;
  }
  .canvas { position: relative; width: 1200px; height: 904px; }

  .panel { position: absolute; overflow: hidden; box-sizing: border-box; }

  /* Top face */
  .top-face { left: 100px; top: 40px; width: 1000px; height: 480px; display: flex; }
  .top-dark {
    position: relative; width: 520px; height: 100%;
    background: linear-gradient(160deg, var(--box-black-light), var(--box-black) 60%);
  }
  .bg-decoration {
    position: absolute; inset: 0;
    background: radial-gradient(ellipse at 45% 55%, rgba(150,150,150,0.28), rgba(150,150,150,0) 70%);
  }
  .brand-lockup { position: absolute; display: flex; align-items: center; gap: 14px; }
  .top-dark .brand-lockup { left: 60px; top: 70px; }
  .brand-square { background: var(--brand-red); border-radius: 10px; }
  .top-dark .brand-square { width: 120px; height: 120px; }
  .brand-name-light { color: var(--white); font-weight: 800; }
  .top-dark .brand-name-light { font-size: 56px; }
  .product-title { position: absolute; left: 60px; right: 40px; bottom: 90px; color: var(--white); font-weight: 700; font-size: 20px; line-height: 1.3; margin: 0; }
  .product-count { position: absolute; left: 60px; bottom: 62px; color: var(--white); font-weight: 400; font-size: 18px; margin: 0; }

  .top-grey { position: relative; flex: 1; background: var(--panel-grey); }
  .red-rule { position: absolute; height: 2px; background: var(--brand-red); }
  .top-grey .rule-a { left: 30px; right: 30px; top: 60px; }
  .top-grey .rule-b { left: 30px; right: 30px; top: 230px; }
  .brand-name-dark { position: absolute; color: var(--ink); font-weight: 800; margin: 0; line-height: 1; white-space: nowrap; }
  .top-grey .brand-name-dark { left: 40px; top: 95px; font-size: 96px; }

  .size-badge { position: absolute; display: flex; flex-direction: column; }
  .size-letter { background: var(--brand-red); color: var(--white); font-weight: 800; text-align: center; line-height: 1; }
  .size-word { background: var(--box-black); color: var(--white); text-align: center; }
  .top-grey .size-badge { right: 40px; top: 270px; width: 110px; }
  .top-grey .size-letter { font-size: 54px; padding: 8px 0; }
  .top-grey .size-word { font-size: 15px; padding: 2px 0; }

  .glove-icon { position: absolute; }
  .top-grey .glove-icon { left: 60px; top: 280px; }

  .feature-list { position: absolute; list-style: none; margin: 0; padding: 0; text-align: right; color: var(--feature-text); font-weight: 600; white-space: nowrap; }
  .feature-list li::after { content: " \2022"; color: var(--brand-red); }
  .top-grey .feature-list { right: 165px; top: 280px; font-size: 20px; line-height: 1.35; }

  /* Front face */
  .front-face {
    left: 100px; top: 540px; width: 1000px; height: 160px;
    background: linear-gradient(180deg, var(--box-black-light), var(--box-black));
  }
  .front-face .product-title { left: 40px; right: 40px; top: 44px; bottom: auto; font-size: 30px; }
  .front-sub { position: absolute; left: 40px; top: 92px; color: var(--white); font-size: 16px; margin: 0; }

  /* End faces */
  .end-dark {
    left: 100px; top: 720px; width: 480px; height: 164px;
    background: linear-gradient(160deg, var(--box-black-light), var(--box-black));
  }
  .end-dark .brand-lockup { left: 24px; top: 20px; }
  .end-dark .brand-square, .end-grey .brand-square { width: 46px; height: 46px; border-radius: 6px; }
  .end-dark .brand-name-light { font-size: 32px; }
  .end-dark .count { position: absolute; left: 24px; bottom: 18px; color: var(--white); font-size: 14px; font-weight: 700; margin: 0; }
  .end-dark .feature-list { right: 116px; top: 18px; font-size: 15px; line-height: 1.3; color: #cfcfcf; }
  .end-dark .size-badge { right: 24px; top: 20px; width: 56px; }
  .end-dark .size-letter, .end-grey .size-letter { font-size: 30px; padding: 6px 0; }
  .end-dark .size-word, .end-grey .size-word { font-size: 11px; padding: 1px 0; }
  .end-dark .size-word { background: #555555; }
  .single-use { position: absolute; font-size: 12px; font-weight: 600; margin: 0; white-space: nowrap; }
  .end-dark .single-use { right: 18px; bottom: 18px; color: var(--white); }

  .end-grey { left: 620px; top: 720px; width: 480px; height: 164px; background: var(--panel-grey); }
  .end-grey .rule-a { left: 100px; right: 24px; top: 14px; }
  .end-grey .rule-b { left: 100px; right: 24px; top: 70px; }
  .end-grey .logo-mark { position: absolute; left: 30px; top: 20px; }
  .end-grey .brand-name-dark { left: 100px; top: 20px; font-size: 44px; }
  .end-grey .glove-icon { left: 110px; top: 80px; }
  .end-grey .size-badge { left: 210px; top: 78px; width: 56px; }
  .end-grey .single-use { left: 100px; bottom: 8px; color: var(--ink); }
</style>
</head>
<body>
<main class="canvas">

  <section class="panel top-face">
    <div class="top-dark">
      <div class="bg-decoration" role="img" aria-label="Faded background decoration behind the top panel"></div>
      <div class="brand-lockup">
        <span class="brand-square"></span>
        <span class="brand-name-light">Brenvo</span>
      </div>
      <p class="product-title">Nitrile Powder Free Black Examination Gloves</p>
      <p class="product-count">100 Gloves by Weight</p>
    </div>
    <div class="top-grey">
      <span class="red-rule rule-a"></span>
      <h1 class="brand-name-dark">Brenvo</h1>
      <span class="red-rule rule-b"></span>
      <svg class="glove-icon" width="90" height="90" viewBox="0 0 90 90" aria-label="Glove icon" role="img">
        <path d="M28 86 L26 52 L12 38 Q8 32 14 30 L30 42 L30 12 Q30 6 35 6 Q40 6 40 12 L40 36 L42 8 Q42 3 47 3 Q52 3 52 8 L52 36 L55 12 Q56 7 61 8 Q65 9 64 14 L62 40 L68 22 Q70 17 74 19 Q78 21 76 26 L66 60 L64 86 Z" fill="none" stroke="var(--glove-blue)" stroke-width="3" stroke-linejoin="round"/>
      </svg>
      <ul class="feature-list">
        <li>Textured</li>
        <li>Non-Sterile</li>
        <li>Ambidextrous</li>
        <li>Latex Free</li>
      </ul>
      <div class="size-badge">
        <span class="size-letter">L</span>
        <span class="size-word">Large</span>
      </div>
    </div>
  </section>

  <section class="panel front-face">
    <div class="bg-decoration" role="img" aria-label="Faded background decoration along the front panel"></div>
    <p class="product-title">Nitrile Powder Free Black Examination Gloves</p>
    <p class="front-sub">Powder free disposable examination gloves made of soft nitrile material</p>
  </section>

  <section class="panel end-dark">
    <div class="bg-decoration" role="img" aria-label="Faded background decoration on the end panel"></div>
    <div class="brand-lockup">
      <span class="brand-square"></span>
      <span class="brand-name-light">Brenvo</span>
    </div>
    <p class="count">100 Gloves by Weight</p>
    <ul class="feature-list">
      <li>Textured</li>
      <li>Non-Sterile</li>
      <li>Ambidextrous</li>
      <li>Latex Free</li>
    </ul>
    <div class="size-badge">
      <span class="size-letter">L</span>
      <span class="size-word">Large</span>
    </div>
    <p class="single-use">For Single Use</p>
  </section>

  <section class="panel end-grey">
    <span class="brand-square logo-mark"></span>
    <span class="red-rule rule-a"></span>
    <h2 class="brand-name-dark">Brenvo</h2>
    <span class="red-rule rule-b"></span>
    <svg class="glove-icon" width="46" height="50" viewBox="0 0 90 90" aria-label="Glove icon" role="img">
      <path d="M28 86 L26 52 L12 38 Q8 32 14 30 L30 42 L30 12 Q30 6 35 6 Q40 6 40 12 L40 36 L42 8 Q42 3 47 3 Q52 3 52 8 L52 36 L55 12 Q56 7 61 8 Q65 9 64 14 L62 40 L68 22 Q70 17 74 19 Q78 21 76 26 L66 60 L64 86 Z" fill="none" stroke="var(--glove-blue)" stroke-width="5" stroke-linejoin="round"/>
    </svg>
    <div class="size-badge">
      <span class="size-letter">L</span>
      <span class="size-word">Large</span>
    </div>
    <p class="single-use">For Single Use</p>
  </section>

</main>
</body>
</html>
```